National online rug retailer needs a home page design

See the MatsNowly logo and create a home page design around that color theme. Details are spelled out in word document uploaded below.

Apparently this website did not take my attachement showing the logo and basic requirements.  If you would send me your email address, I will send you the attachment directly.
Best regards,
Ned Ferris
nferris@qorvex.com

Target Market(s)

The target market is home owners 25 to 75 years old with combined incomes over $100,000 per year.

Industry/Entity Type

Online

Requirements
Must have
• Lots of white space with black letters and creative use of red and possibly one other color. Would like a compelling call to action button.

```html
<!DOCTYPE html>
<html lang="en">
<head>
<meta charset="utf-8">
<title>MatsNowly.com – Home</title>
<link href="https://fonts.googleapis.com/css2?family=Arimo:wght@400;700&family=Oswald:wght@400;500;700&display=swap" rel="stylesheet">
<style>
:root{
  --page:#e9e9e9;
  --ink:#111;
  --text:#333;
  --muted:#666;
  --red:#e0161c;
  --bar:#000;
  --panel:#f4f4f4;
  --card:#e4e4e4;
  --line:#d6d6d6;
  --white:#fff;
  --foot:#000;
  --foot-base:#4a4a4a;
}
*{box-sizing:border-box;margin:0;padding:0}
html,body{width:1001px;height:1200px;overflow:hidden}
body{background:var(--page);font-family:"Arimo",Arial,sans-serif;color:var(--text);position:relative;font-size:11px}
a{color:inherit;text-decoration:none}
.abs{position:absolute}

/* header */
.brand{left:128px;top:28px;display:flex;align-items:center;gap:8px}
.brand-mark{width:24px;height:24px;background:var(--red)}
.brand-name{font-family:"Arimo",sans-serif;font-size:31px;font-weight:400;color:var(--red);letter-spacing:-.5px}
.tagline{left:208px;top:79px;font-size:11px;color:var(--muted)}
.search{left:434px;top:22px;width:169px;height:22px;border:1px solid #aaa;border-radius:4px;background:var(--white);display:flex}
.search span{flex:1;font-size:10px;color:#888;padding:4px 8px}
.search i{width:22px;border-left:1px solid #aaa;display:flex;align-items:center;justify-content:center}
.cart{left:644px;top:22px;width:243px;height:24px;border:1px solid #bbb;border-radius:4px;background:#f6f6f6;display:flex;font-size:11px;color:var(--ink)}
.cart span{display:flex;align-items:center;padding:0 7px;border-right:1px solid #ccc}
.cart span:last-child{border:0}
.cart b{display:inline-block;width:24px;height:16px;background:var(--white);border:1px solid #bbb;margin-left:5px}
.tollfree{right:115px;top:60px;display:flex;align-items:baseline;gap:12px;font-size:11px;color:var(--text)}
.tollfree strong{font-family:"Oswald",sans-serif;font-size:19px;color:var(--red);font-weight:500;letter-spacing:.5px}
.account{right:115px;top:87px;font-size:10px;color:var(--text)}

/* nav */
.nav{left:114px;top:106px;width:773px;height:34px;background:var(--bar);border-radius:5px 5px 0 0;display:flex;align-items:center;padding-left:14px;gap:33px}
.nav a{color:var(--white);font-size:12px;letter-spacing:.2px}

.sheet{left:114px;top:140px;width:773px;height:815px;background:var(--white);border:2px solid var(--bar);border-top:0}

/* sidebar */
.sidebar{left:128px;top:151px;width:157px;height:794px;background:#ddd;border:1px solid #ccc}
.browse{left:138px;top:161px;width:138px;height:333px;background:#ececec;border:1px solid #ccc}
.browse-title{left:130px;top:162px;width:130px;height:34px;background:linear-gradient(#f4f4f4,#c8c8c8);font-family:"Oswald",sans-serif;font-weight:700;font-size:17px;color:var(--ink);padding:6px 0 0 20px;box-shadow:0 2px 2px rgba(0,0,0,.25)}
.filters{left:145px;top:197px;width:117px;list-style:none}
.filters li{font-family:"Oswald",sans-serif;font-size:10px;color:var(--ink);text-transform:uppercase;border-bottom:1px dashed #aaa;height:19px;line-height:16px;padding-left:14px;position:relative}
.filters li::before{content:"→";position:absolute;left:0;top:0;font-family:Arimo,sans-serif}
.filters li i{position:absolute;right:0;top:3px;width:9px;height:9px;border:1px solid #999;background:#fff;font-style:normal;font-size:8px;line-height:7px;text-align:center}
.filters li.open{border:0}
.sub{list-style:none;border-bottom:1px dashed #aaa;margin-bottom:3px;padding-bottom:3px}
.sub li{font-family:"Arimo",sans-serif;text-transform:none;font-size:11.5px;color:var(--red);border:0;padding-left:26px;height:19px;line-height:17px}
.sub li::before{left:16px;font-size:9px;color:#777}
.badges{left:138px;top:505px;width:138px;height:430px;background:#ececec;border:1px solid #ccc}
.badge{position:absolute;background:var(--white);border:1px solid #ccc}

/* banner */
.hero{left:301px;top:152px;width:571px;height:205px;background:linear-gradient(100deg,#5a2c22 0%,#8a2f3e 30%,#a0503a 50%,#4a2a1e 70%,#6b4a30 100%)}
.hero-box{left:556px;top:225px;width:260px;height:107px;border:1px solid rgba(255,255,255,.45)}
.hero-kicker{left:571px;top:235px;font-size:17px;color:var(--white);letter-spacing:.3px}
.hero-offer{left:565px;top:247px;font-family:"Oswald",sans-serif;font-weight:700;font-size:60px;color:var(--white);line-height:1.15}
.hero-offer sup{font-size:28px;vertical-align:32px}

/* product panels */
.panel{position:absolute;left:300px;width:573px;height:212px;background:var(--panel);border:1px solid var(--line)}
.panel-title{position:absolute;left:14px;top:6px;display:flex;align-items:center;gap:4px;font-size:18px;color:var(--ink)}
.view-all{position:absolute;right:14px;top:11px;font-size:12px;color:var(--ink);display:flex;align-items:center;gap:3px}
.card{position:absolute;top:36px;width:129px;height:156px;background:var(--card)}
.card .img{position:absolute;left:7px;top:7px;width:115px;height:86px}
.card .name{position:absolute;left:7px;top:98px;font-size:10.5px;color:var(--ink);white-space:nowrap;overflow:hidden;width:118px}
.card .price{position:absolute;left:8px;top:116px;font-family:"Arimo",sans-serif;font-weight:700;font-size:14px;color:var(--red)}
.card .was{position:absolute;left:7px;top:116px;font-weight:700;font-size:13px;color:var(--red);text-decoration:line-through;text-decoration-color:#000}
.card .now{position:absolute;left:7px;top:132px;font-weight:700;font-size:13px;color:var(--red)}
.card .buy{position:absolute;left:73px;top:116px;width:50px;height:18px;background:var(--bar);color:var(--white);font-size:10px;text-align:center;line-height:18px}
.img.a{background:linear-gradient(135deg,#c7a6c1,#7b5b74 55%,#2f2a33)}
.img.b{background:linear-gradient(135deg,#b7b1a8,#8f887f)}
.img.c{background:linear-gradient(135deg,#6d93b3,#9fb7c8)}
.img.d{background:linear-gradient(135deg,#d8d2cb,#a79d92)}

/* testimonials */
.reviews{left:300px;top:825px;width:573px;height:117px;background:var(--panel);border:1px solid var(--line)}
.reviews h3{position:absolute;left:108px;top:8px;display:flex;align-items:center;gap:6px;font-weight:400;font-size:12px;color:var(--red);letter-spacing:.3px}
.quote{position:absolute;left:19px;top:31px;width:534px;height:81px;background:#e2e2e2;border:1px solid #d0d0d0;padding:6px 14px;font-size:10px;line-height:12.6px;color:var(--ink);text-align:center}
.quote cite{display:block;font-style:normal;color:var(--red);font-size:12px;margin-top:1px}

/* footer */
.footer{left:0;top:955px;width:1001px;height:213px;background:var(--foot);color:var(--white)}
.fcol{position:absolute;top:10px}
.fcol h4{font-weight:400;font-size:16px;letter-spacing:.2px;margin-bottom:8px}
.fcol ul{list-style:none;font-size:11px;line-height:16.7px}
.frule{position:absolute;left:128px;top:33px;width:744px;height:1px;background:#444}
.social{display:flex;gap:10px;margin-top:4px}
.social span{width:31px;height:31px;background:var(--red);border-radius:4px}
.copy{left:0;top:1168px;width:1001px;height:32px;background:var(--foot-base);color:#bbb;font-size:8px;text-align:center;line-height:34px;letter-spacing:.5px}
</style>
</head>
<body>

<header>
  <a class="abs brand" href="#"><span class="brand-mark"></span><span class="brand-name">MatsNowly.com</span></a>
  <p class="abs tagline">for domestic and heirloom values</p>
  <form class="abs search"><span>enter key words or item #</span><i><svg width="11" height="11" viewBox="0 0 11 11"><circle cx="4.5" cy="4.5" r="3.5" fill="none" stroke="#555" stroke-width="1.5"/><line x1="7" y1="7" x2="10.5" y2="10.5" stroke="#555" stroke-width="1.5"/></svg></i></form>
  <div class="abs cart"><span>Items<b></b></span><span>Total $00</span><span>View Cart</span><span>Checkout</span></div>
  <p class="abs tollfree">Order toll-free: <strong>1-888-555-0142</strong></p>
  <p class="abs account">My Account | Sign In ● LIVE CHAT ● ONLINE</p>
</header>

<nav class="abs nav">
  <a href="#">HOME</a><a href="#">SELECTION GUIDES</a><a href="#">RUG CARE</a><a href="#">FAQ</a><a href="#">RETURN POLICY</a><a href="#">FREE SHIPPING</a><a href="#">CLEARANCE RUGS</a>
</nav>

<div class="abs sheet"></div>

<aside>
  <div class="abs sidebar"></div>
  <div class="abs browse"></div>
  <div class="abs browse-title">BROWSE</div>
  <ul class="abs filters">
    <li class="open">Rug Theme<i>-</i></li>
    <ul class="sub"><li>Traditional</li><li>Transitional</li><li>Casual</li></ul>
    <li class="open">Color Way<i>-</i></li>
    <ul class="sub"><li>Black</li><li>Blue</li><li>Green</li><li>Gold</li></ul>
    <li>Size<i>+</i></li>
    <li>Shape<i>+</i></li>
    <li>Fiber Content<i>+</i></li>
    <li>Mfgr. Brand<i>+</i></li>
    <li>Mfgr.Collection<i>+</i></li>
    <li>Price<i>+</i></li>
  </ul>
  <div class="abs badges" role="img" aria-label="Accepted payment methods and security seals">
    <span class="badge" style="left:9px;top:15px;width:52px;height:34px;background:#d33"></span>
    <span class="badge" style="left:73px;top:15px;width:52px;height:34px"></span>
    <span class="badge" style="left:9px;top:61px;width:52px;height:32px;background:#dfe3ef"></span>
    <span class="badge" style="left:73px;top:61px;width:52px;height:32px;background:#3a78b5"></span>
    <span class="badge" style="left:9px;top:105px;width:52px;height:33px"></span>
    <span class="badge" style="left:73px;top:105px;width:52px;height:33px"></span>
    <span class="badge" style="left:9px;top:150px;width:52px;height:58px"></span>
    <span class="badge" style="left:73px;top:150px;width:52px;height:58px"></span>
    <span class="badge" style="left:7px;top:222px;width:119px;height:50px"></span>
    <span class="badge" style="left:7px;top:285px;width:119px;height:58px;background:#1d5a8e"></span>
    <span class="badge" style="left:7px;top:355px;width:119px;height:52px"></span>
  </div>
</aside>

<main>
  <div class="abs hero" role="img" aria-label="Rug showroom with stacked colorful woven rugs"></div>
  <div class="abs hero-box"></div>
  <p class="abs hero-kicker">SUMMER INSPIRATIONS</p>
  <p class="abs hero-offer">SAVE 20<sup>%</sup></p>

  <section class="panel" style="top:373px">
    <h2 class="panel-title"><svg width="34" height="22" viewBox="0 0 34 22"><rect x="0" y="8" width="4" height="4" fill="#bbb"/><rect x="6" y="5" width="4" height="4" fill="#bbb"/><rect x="6" y="12" width="4" height="4" fill="#bbb"/><path d="M12 5h10V0l12 11-12 11v-5H12z" fill="#aaa"/></svg><span style="font-weight:400">Latest Products</span></h2>
    <a class="view-all" href="#">View All <svg width="12" height="12" viewBox="0 0 12 12"><path d="M1 1l5 5-5 5M6 1l5 5-5 5" fill="none" stroke="#e0161c" stroke-width="1.6"/></svg></a>
    <article class="card" style="left:11px"><div class="img a" role="img" aria-label="Abstract pastel rug"></div><p class="name">Lorem Ipsum proin gravi</p><p class="price">$500</p><a class="buy" href="#">Buy Now</a></article>
    <article class="card" style="left:151px"><div class="img b" role="img" aria-label="Taupe rug with ring pattern"></div><p class="name">Lorem Ipsum proin gravi</p><p class="price">$500</p><a class="buy" href="#">Buy Now</a></article>
    <article class="card" style="left:291px"><div class="img c" role="img" aria-label="Blue scroll pattern rug"></div><p class="name">Lorem Ipsum proin gravi</p><p class="price">$500</p><a class="buy" href="#">Buy Now</a></article>
    <article class="card" style="left:431px"><div class="img d" role="img" aria-label="Ivory rug with branch pattern"></div><p class="name">Lorem Ipsum proin gravi</p><p class="price">$500</p><a class="buy" href="#">Buy Now</a></article>
  </section>

  <section class="panel" style="top:599px">
    <h2 class="panel-title"><svg width="34" height="22" viewBox="0 0 34 22"><rect x="0" y="8" width="4" height="4" fill="#bbb"/><rect x="6" y="5" width="4" height="4" fill="#bbb"/><rect x="6" y="12" width="4" height="4" fill="#bbb"/><path d="M12 5h10V0l12 11-12 11v-5H12z" fill="#aaa"/></svg><span style="font-weight:400">Clearance Sale</span></h2>
    <a class="view-all" href="#">View All <svg width="12" height="12" viewBox="0 0 12 12"><path d="M1 1l5 5-5 5M6 1l5 5-5 5" fill="none" stroke="#e0161c" stroke-width="1.6"/></svg></a>
    <article class="card" style="left:11px"><div class="img a" role="img" aria-label="Abstract pastel rug"></div><p class="name">Lorem Ipsum proin gravi</p><p class="was">$400</p><p class="now">$100</p><a class="buy" href="#">Buy Now</a></article>
    <article class="card" style="left:151px"><div class="img b" role="img" aria-label="Taupe rug with ring pattern"></div><p class="name">Lorem Ipsum proin gravi</p><p class="was">$400</p><p class="now">$100</p><a class="buy" href="#">Buy Now</a></article>
    <article class="card" style="left:291px"><div class="img c" role="img" aria-label="Blue scroll pattern rug"></div><p class="name">Lorem Ipsum proin gravi</p><p class="was">$400</p><p class="now">$100</p><a class="buy" href="#">Buy Now</a></article>
    <article class="card" style="left:431px"><div class="img d" role="img" aria-label="Ivory rug with branch pattern"></div><p class="name">Lorem Ipsum proin gravi</p><p class="was">$400</p><p class="now">$100</p><a class="buy" href="#">Buy Now</a></article>
  </section>

  <section class="abs reviews">
    <h3><svg width="26" height="18" viewBox="0 0 26 18"><ellipse cx="9" cy="7" rx="9" ry="6" fill="#2a8fd6"/><path d="M4 11l-2 5 6-4z" fill="#2a8fd6"/><ellipse cx="18" cy="10" rx="7" ry="5" fill="#7cc0ec"/></svg>WHAT OUR CUSTOMERS ARE SAYING ABOUT</h3>
    <blockquote class="quote">Lorem Ipsum. Proin gravida nibh vel velit auctor aliquet. Aenean sollicitudin, lorem quis bibendum auctor, nisi elit consequat ipsum, nec sagittis sem nibh id elit. Duis sed odio sit amet nibh vulputate cursus a sit amet mauris. Morbi accumsan ipsum velit. Nam nec tellus a odio tincidunt auctor a ornare odio. Sed non mauris vitae erat consequat auctor eu in elit. Class aptent taciti sociosqu ad litora torquent per conubia<cite>Karen T. &nbsp; CA</cite></blockquote>
  </section>
</main>

<footer class="abs footer">
  <div class="frule"></div>
  <div class="fcol" style="left:128px"><h4>Customer Service</h4><ul><li>Shipping</li><li>Return Policy</li><li>Privacy Policy</li><li>Ordering &amp; Delivery</li><li>Checklist</li><li>Terms of Use</li><li>Terms of Sale</li><li>Contact Us</li><li>Environmental Policy</li></ul></div>
  <div class="fcol" style="left:357px"><h4>Resources</h4><ul><li>Product Articles</li><li>Learning Center</li><li>Help</li><li>Refer A Friend</li><li>MatsNowly Blog</li><li>Room Scene Viewer</li><li>Site Map</li><li>FAQ</li><li>Customer Testimonials</li><li>Photo Gallery</li></ul></div>
  <div class="fcol" style="left:554px"><h4>Corporate Info</h4><ul><li>About MatsNowly.com</li><li>Careers</li><li>Affiliates</li></ul></div>
  <div class="fcol" style="left:741px"><h4>Be Social with US</h4><div class="social" aria-label="Social links"><span></span><span></span><span></span></div></div>
</footer>
<p class="abs copy">Copyright © 2013 MatsNowly. All right reserved.</p>

</body>
</html>
```